EILT: Landing Page - EXPRESS VERSAND
Zielgruppe
Es soll in kurzer Zeit (max 48 Stunden) eine kleine Ladingpage entstehen. Expressversand / Import von China nach Deutschland . Aufgrund der stark steigenden Luftfrachtraten aus China heraus hat sich unsere Firma Fracht-Kapazitäten gesichert. Diese sollen nun angeboten werden. Über eine Ladingpage sollen Anfragen generiert werden. Diese Anfragen werden dann mit einem Angebot von uns beantwortet. Expressversand / Import von China nach Deutschland
Aufgabenstellung
Die Seite soll beinhalten:
- 1-2 Bilder (z. B. Luftfracht, Logistik, Flugzeug, Cargo, etc)
- kurzer erklärender Text: z.B. 'jetzt Angebot anfordern und günstig aus China per Express versenden.' Inkl. Abholung, Verzollung und Zustellung. Kurze Laufzeit von nur 3-5 Tagen. ab 45€ / Paket
- Anfrage Formular, bestehend aus: , Abholadresse in China/Post Code, ZielAdresse Deutschland, Sendungsinformationen (wie viele Kartons, wie schwer ist ein Karton und welche Abmessungen L/B/H ), wann ist die Sendung in China abholbereit, optional: Sendungsinhalt (Ware, Zolltarifnummer/HS Code) , Firma, Name, email adresse
- optional ein Header/Laufband etc mit: Bis zum 19. Nov 21 versenden - Ware bis GrauSonntag erhalten!
- 24h Servicehotline, Tel: 0987/213546
- 2-3 Kundenreferenzen: Bilder von Personen mit Text : „Schneller Versand - nur 4 Tage Laufzeit“ , „1A Service, ohne Probleme“ , „gute Preise - nur zu empfehlen.“
Unser Firmenlogo kann - muss aber nicht auftauchen.
In der farblichen Gestaltung haben Sie freie Hand und freuen uns auf Ihre Vorschläge.
Aufgrund der Dringlichkeit sollte diese Landingpage innerhalb 48 Stunden 'live ' gehen.
WICHTIG: Die Page sollte von Ihnen auch veröffentlich werden. Aktuell nutzen wir den Kelvo Homepagebaukasten. Die Page kann aber auch durch andere Anbieter veröffentlicht werden , zb Pagimundo

```html
<!DOCTYPE html>
<html lang="de">
<head>
<meta charset="utf-8">
<title>Expressversand China – Deutschland</title>
<link rel="stylesheet" href="https://fonts.googleapis.com/css2?family=Roboto:wght@400;500;700&family=Source+Sans+3:wght@400;600;700&display=swap">
<style>
:root{
  --blue:#29abe2;
  --red:#e0355a;
  --purple:#8b55d9;
  --coral:#d16562;
  --ink:#222;
  --field:#ffffff;
  --panel:rgba(255,255,255,.55);
  --footer:#e6e6e6;
}
*{box-sizing:border-box;margin:0;padding:0}
html,body{width:1182px;height:1200px;overflow:hidden;background:#fff}
body{position:relative;font-family:'Roboto',sans-serif;color:var(--ink)}
.promo-bar{position:absolute;left:0;top:0;width:1182px;height:48px;background:var(--blue);color:#fff;font-size:14px;font-weight:500;display:flex;align-items:center;justify-content:center;letter-spacing:.1px}
.promo-line{position:absolute;left:0;top:48px;width:1182px;height:4px;background:var(--red)}
.hero{position:absolute;left:0;top:52px;width:1182px;height:799px;background:linear-gradient(180deg,#7a5cc9 0%,#b65aa8 35%,#a06cc0 60%,#8a5ec6 100%)}
.brand{position:absolute;left:59px;top:84px;display:flex;align-items:center;gap:8px}
.brand-dot{width:40px;height:40px;border-radius:50%;background:var(--blue)}
.brand-name{font-size:22px;font-weight:700;color:#fff}
.hero-kicker{position:absolute;left:0;top:82px;width:1182px;text-align:center;color:#fff;font-size:23px;font-weight:400}
.hero-title{position:absolute;left:0;top:106px;width:1182px;text-align:center;color:#fff;font-size:46px;font-weight:700;letter-spacing:.3px}
.hotline{position:absolute;left:488px;top:171px;width:207px;height:49px;border:2px solid #fff;border-radius:25px;background:var(--red);color:#fff;display:flex;align-items:center;padding-left:20px;gap:12px}
.hotline-label{font-size:10.5px;line-height:1}
.hotline-number{font-size:18px;font-weight:700;margin-top:4px;line-height:1}
.hero-sub{position:absolute;left:0;top:244px;width:1182px;text-align:center;color:#fff;font-size:15px}
.request-form{position:absolute;left:191px;top:279px;width:800px;height:351px;background:var(--panel);border-radius:9px}
.lbl{position:absolute;font-size:9.5px;color:#222;white-space:nowrap}
.fld{position:absolute;height:31px;background:var(--field);font-size:9.5px;color:#777;padding:10px 0 0 10px}
.fld.area{height:90px;padding-top:15px;line-height:1.25}
.consent{position:absolute;left:27px;top:300px;display:flex;align-items:center;gap:8px;font-size:11px}
.consent-box{width:24px;height:20px;background:#fff}
.submit{position:absolute;left:283px;top:290px;width:146px;height:41px;border:2px solid #fff;border-radius:21px;background:var(--red);color:#fff;font-size:15px;font-weight:500;display:flex;align-items:center;justify-content:center}
.feature{position:absolute;top:674px;width:177px;height:139px;background:#fff;border-radius:9px;text-align:center;font-size:10.5px;line-height:1.6}
.feature-icon{position:absolute;left:58px;top:17px;width:60px;height:60px;border-radius:8px;background:linear-gradient(135deg,#2fb8e6,#f2a23a)}
.feature-text{position:absolute;left:0;width:100%}
.reviews-title{position:absolute;left:0;top:892px;width:1260px;text-align:center;font-family:'Source Sans 3',sans-serif;font-size:27px;font-weight:600;color:#111}
.review{position:absolute;top:943px;width:284px;height:125px;color:#fff;font-family:'Source Sans 3',sans-serif}
.review-quote{position:absolute;left:0;top:16px;width:100%;text-align:center;font-size:15px}
.review-avatar{position:absolute;top:50px;width:53px;height:53px;border-radius:50%;background:linear-gradient(160deg,#7a5a48,#2b2420)}
.review-name{position:absolute;top:64px;font-size:12px}
.review-stars{position:absolute;top:79px;font-size:10px;color:#f7b731;letter-spacing:.5px}
.footer{position:absolute;left:0;top:1102px;width:1182px;height:45px;background:var(--footer);display:flex;align-items:center;justify-content:center;font-family:'Source Sans 3',sans-serif;font-size:12.5px;padding-left:80px}
</style>
</head>
<body>
<div class="promo-bar">BIS ZUM 19. NOVEMBER 2021 VERSENDEN – WARE BIS GRAUSONNTAG ERHALTEN!</div>
<div class="promo-line"></div>

<section class="hero" role="img" aria-label="Hafen mit Containern, Lkw und startendem Frachtflugzeug in violettem Farbton"></section>

<div class="brand"><span class="brand-dot"></span><span class="brand-name">Velkaro</span></div>
<div class="hero-kicker">EXPRESSVERSAND IMPORT VON</div>
<h1 class="hero-title">CHINA NACH DEUTSCHLAND</h1>
<div class="hotline">
  <svg width="26" height="26" viewBox="0 0 24 24" fill="#fff" aria-hidden="true"><path d="M6.6 10.8a15.1 15.1 0 0 0 6.6 6.6l2.2-2.2c.3-.3.7-.4 1-.2 1.1.4 2.3.6 3.6.6.6 0 1 .4 1 1V20c0 .6-.4 1-1 1A17 17 0 0 1 3 4c0-.6.4-1 1-1h3.5c.6 0 1 .4 1 1 0 1.3.2 2.5.6 3.6.1.3 0 .7-.2 1z"/></svg>
  <div><div class="hotline-label">24H SERVICEHOTLINE</div><div class="hotline-number">0987/213546</div></div>
</div>
<p class="hero-sub">jetzt Anfrage stellen - Angebot erhalten - günstig per Express versenden</p>

<form class="request-form">
  <span class="lbl" style="left:27px;top:40px">Wie viele Kartons sollen versendet werden?</span>
  <span class="lbl" style="left:278px;top:40px">Gewicht pro Karton in kg</span>
  <span class="lbl" style="left:529px;top:40px">Ab wann können wir die Sendung abholen?</span>
  <div class="fld" style="left:27px;top:52px;width:239px">Wie viele Kartons sollen versendet werden?</div>
  <div class="fld" style="left:278px;top:52px;width:239px">Gewicht pro Karton in kg</div>
  <div class="fld" style="left:529px;top:52px;width:239px">Ab wann können wir die Sendung abholen?</div>

  <span class="lbl" style="left:27px;top:104px">Abmessung pro Karton in cm (L/B/H)</span>
  <span class="lbl" style="left:278px;top:104px">Wo dürfen wird die Sendung abholen?</span>
  <span class="lbl" style="left:529px;top:104px">Wohin sollen wir die Sendung liefern?</span>
  <div class="fld" style="left:27px;top:115px;width:72px">Länge</div>
  <div class="fld" style="left:110px;top:115px;width:73px">Breite</div>
  <div class="fld" style="left:194px;top:115px;width:72px">Höhe</div>
  <div class="fld" style="left:278px;top:115px;width:72px">Postleitzahl</div>
  <div class="fld" style="left:361px;top:115px;width:73px">Ort</div>
  <div class="fld" style="left:445px;top:115px;width:72px">Land</div>
  <div class="fld" style="left:529px;top:115px;width:72px">Postleitzahl</div>
  <div class="fld" style="left:612px;top:115px;width:73px">Ort</div>
  <div class="fld" style="left:696px;top:115px;width:72px">Land</div>

  <span class="lbl" style="left:27px;top:168px">Was wird verschickt? (Ware/Zolltarifnummer/HS Code)</span>
  <span class="lbl" style="left:278px;top:168px">Müssen wir noch etwas über diese Sendungen wissen?</span>
  <span class="lbl" style="left:529px;top:168px">Vorname</span>
  <span class="lbl" style="left:662px;top:168px">Nachname</span>
  <div class="fld area" style="left:27px;top:180px;width:239px">Was wird verschickt? (Ware/Zolltarifnummer/<br>HS Code)</div>
  <div class="fld area" style="left:278px;top:180px;width:239px">Müssen wir noch etwas über diese Sendungen<br>wissen?</div>
  <div class="fld" style="left:529px;top:180px;width:106px">Vorname</div>
  <div class="fld" style="left:662px;top:180px;width:106px">Nachname</div>
  <span class="lbl" style="left:529px;top:226px">Firma</span>
  <span class="lbl" style="left:662px;top:226px">E-Mail</span>
  <div class="fld" style="left:529px;top:238px;width:106px">Firma</div>
  <div class="fld" style="left:662px;top:238px;width:106px">E-Mail</div>

  <label class="consent"><span class="consent-box"></span>Ich stimme der Datenschutzerklärung zu</label>
  <div class="submit">Versand anfragen</div>
</form>

<div class="feature" style="left:207px"><div class="feature-icon" role="img" aria-label="Symbol Globus mit Flugzeug und Paket"></div><div class="feature-text" style="top:88px">Verzollung und Zustellung<br>bis vor die Tür</div></div>
<div class="feature" style="left:404px"><div class="feature-icon" role="img" aria-label="Symbol Stoppuhr"></div><div class="feature-text" style="top:88px">kurze Laufzeit von nur<br>3-5 Tagen</div></div>
<div class="feature" style="left:601px"><div class="feature-icon" role="img" aria-label="Symbol Route mit Standortmarker"></div><div class="feature-text" style="top:100px">inkl. Sendungsverfolgung</div></div>
<div class="feature" style="left:798px"><div class="feature-icon" role="img" aria-label="Symbol Geldbörse und Smartphone"></div><div class="feature-text" style="top:96px">Zahlung auf Rechnung</div></div>

<h2 class="reviews-title">Was under Kunde sagt</h2>

<div class="review" style="left:190px;background:var(--purple)">
  <div class="review-quote">Schneller Versand - nur 4 Tage Laufzeit</div>
  <div class="review-avatar" style="left:69px" role="img" aria-label="Kundenfoto"></div>
  <div class="review-name" style="left:130px">Lenno Varik</div>
  <div class="review-stars" style="left:130px">★★★★★</div>
</div>
<div class="review" style="left:488px;background:var(--coral)">
  <div class="review-quote">1A Service, ohne Probleme</div>
  <div class="review-avatar" style="left:82px" role="img" aria-label="Kundenfoto"></div>
  <div class="review-name" style="left:147px">Timo Kessler</div>
  <div class="review-stars" style="left:144px">★★★★★</div>
</div>
<div class="review" style="left:787px;background:var(--blue)">
  <div class="review-quote">Gute Preise - nur zu empfehlen.</div>
  <div class="review-avatar" style="left:81px" role="img" aria-label="Kundenfoto"></div>
  <div class="review-name" style="left:143px">Lenno Varik</div>
  <div class="review-stars" style="left:143px">★★★★★</div>
</div>

<footer class="footer">Copyright 2021. Alle Rechte vorbehalten.</footer>
</body>
</html>
```